Business school needs a web design

Who We are:
KRVT is a small business school that offers programs in Project Management. The school is based in West Africa and welcomes students from the whole area. Our aim is to become one of the reference business schools in Africa.

Project Brief:
The site will include all informations relevant for different types of visitors that we have: actual and future students, companies, mass media, future employees, ect. It will present information about subscription, list of programs, presentation of the school and its team,etc.

What We want:
This competition is for Design only no coding! We need design for two pages.
We did some wireframing for the home page and the list of programs page. We made them just to show how we imagine the website would look like. But we encourage creative designs, so you don't have to stick to the wireframe models.

Sites We like:
http://www.ravenmoorcollege.example/
http://www.belvantis.example/fr/etudes.html
http://www.qtl.example/mba/Pages/default.aspx

Color schemes
The logo of the school is red and black. So the color scheme of the website should match that. For the rest, it is opened to your imagination.
Updates

The payment for the project is now garanteed. Good luck to you all !

Target Market(s)

The target market is diversified because we have students of different ages, also company representatives or employees that might visit the website for recruitment purposes. But the majority of our audience should be aged between 20 - 30 years.

Industry/Entity Type

Small Business

Requirements
Must have
• The design must include two pages: a home page and another interior page : might be the list of programs or any other page relevant to the domain. The Home page must include a slide show at the beginning.
The background page must be white.
Nice to have
• The use of flat design for this project is preferred.
The use of Pelican scaffold as a base for the design is an asset.

```html
<!DOCTYPE html>
<html lang="fr">
<head>
<meta charset="utf-8">
<title>KRVT — Ecole de gestion</title>
<link href="https://fonts.googleapis.com/css2?family=Open+Sans:wght@400;600;700&display=swap" rel="stylesheet">
<style>
:root{
  --red:#c8070d;
  --ink:#1c1c1c;
  --text:#555;
  --muted:#888;
  --line:#d9d9d9;
  --hero:#f3f3f3;
  --band:#595959;
  --foot:#e4e4e4;
  --photo-a:#a9a9a9;
  --photo-b:#c9b8a6;
}
*{box-sizing:border-box;margin:0;padding:0}
html,body{width:944px;height:1200px;overflow:hidden;background:#fff}
body{font-family:"Open Sans",Arial,sans-serif;color:var(--text);position:relative}
.abs{position:absolute}
a{color:inherit;text-decoration:none}
.red{color:var(--red)}

/* header */
.brand{left:45px;top:24px;display:flex;align-items:center;gap:8px}
.brand-mark{width:22px;height:22px;background:var(--red)}
.brand-name{font-size:24px;font-weight:700;color:var(--ink);letter-spacing:1px}
.toplinks{right:69px;top:15px;font-size:11px;color:var(--muted);display:flex}
.toplinks span{padding:0 7px;border-left:1px solid var(--line)}
.toplinks span:first-child{border:none}
.toplinks span:last-child{padding-right:0}
.search{left:719px;top:45px;width:164px;height:23px;border:1px solid var(--line);border-radius:3px;font-size:10px;color:var(--muted);padding:4px 8px}
.search-btn{position:absolute;right:-1px;top:-1px;width:29px;height:23px;background:var(--red);border-radius:0 3px 3px 0}
.mainnav{right:61px;top:84px;font-size:11.5px;color:#333;display:flex}
.mainnav span{padding:0 7px;border-left:1px solid var(--line)}
.mainnav span:first-child{border:none;color:var(--red)}
.mainnav span:last-child{padding-right:0}
.header-rule{left:0;top:106px;width:944px;height:2px;background:#d4d4d4}

/* hero */
.hero{left:0;top:108px;width:944px;height:262px;background:linear-gradient(#f7f7f7,#ededed);border-bottom:2px solid #d4d4d4}
.hero-scene{right:0;top:0;width:560px;height:260px;background:radial-gradient(ellipse at 40% 55%,#e2e2e2,rgba(236,236,236,0) 60%)}
.hero h1{left:45px;top:72px;font-size:21px;font-weight:700;color:var(--ink)}
.hero p{left:45px;top:107px;font-size:11.5px;color:#222;line-height:24.6px;width:480px}

/* boxes */
.box{border:1px solid var(--line);background:#fff}
.box-title{font-size:16px;font-weight:600;color:var(--ink)}
.who{left:45px;top:390px;width:190px;height:215px}
.who .box-title{position:absolute;left:14px;top:8px}
.who ul{list-style:none;position:absolute;left:16px;top:36px;width:156px}
.who li{font-size:10.5px;color:#444;height:24.6px;line-height:24px;border-bottom:1px solid #eee;padding-left:2px}
.who li:last-child{border:none}
.tv{left:45px;top:615px;width:190px;height:229px}
.tv .box-title{position:absolute;left:14px;top:9px}
.tv-frame{position:absolute;left:14px;top:38px;width:161px;height:124px;background:linear-gradient(135deg,#8b8e96,#c9c0b8 60%,#7a7f88)}
.tv-bar{position:absolute;left:14px;top:162px;width:161px;height:30px;background:#a5a5a5}
.tv-more{position:absolute;left:14px;top:202px;font-size:10.5px;color:var(--red)}

/* centre */
.section-title{font-size:16px;font-weight:600;color:var(--ink)}
.rule{height:1px;background:var(--line)}
.intro{left:257px;top:420px;width:410px;font-size:10.5px;line-height:19px;color:#666}
.post{width:122px;top:524px}
.post .thumb{height:84px}
.post .date{font-size:10px;font-weight:700;color:var(--ink);margin-top:8px}
.post p{font-size:10.3px;line-height:15.6px;color:#555;margin-top:4px}
.post .more{font-size:10.5px;color:var(--red);margin-top:5px}
.event{left:257px;width:412px;height:50px}
.event .cal{position:absolute;left:0;top:0;width:55px;height:49px;border:1px solid var(--line);background:#fff;text-align:center}
.event .cal b{display:block;background:var(--red);color:#fff;font-size:10.5px;height:24px;line-height:24px}
.event .cal span{display:block;font-size:14px;font-weight:700;color:#333;line-height:24px}
.event h3{position:absolute;left:67px;top:-3px;font-size:10.5px;font-weight:700;color:var(--ink)}
.event p{position:absolute;left:67px;top:14px;font-size:10.3px;line-height:15.6px;color:#555;width:340px}

/* news */
.news{left:692px;top:390px;width:190px;height:452px}
.news .box-title{position:absolute;left:15px;top:5px}
.news-item{position:absolute;left:16px;width:170px}
.news-item .thumb{position:absolute;left:0;top:0;width:66px;height:56px}
.news-item p{position:absolute;left:73px;top:-3px;width:90px;font-size:9.3px;line-height:15.6px;color:#555}
.news-item p b{color:var(--ink);font-weight:700}
.news-more{position:absolute;left:16px;top:403px;font-size:10.5px;color:var(--red)}

/* share rail */
.rail{left:910px;top:392px;width:34px;height:172px;border:1px solid var(--line);border-right:none;background:#f4f4f4}
.rail div{height:34px;border-bottom:1px solid var(--line);display:flex;align-items:center;justify-content:center}
.rail div:last-child{border:none}

/* partners */
.partners{left:45px;top:901px;width:837px;height:81px;display:flex;align-items:center;justify-content:space-around;padding:0 14px}
.partner{background:#cfcfcf;border-radius:4px}

/* footer */
.band{left:0;top:999px;width:944px;height:34px;background:var(--band)}
.band h4{position:absolute;top:9px;font-size:11.5px;font-weight:600;color:#fff}
.foot{left:0;top:1033px;width:944px;height:136px;background:var(--foot)}
.foot ul{list-style:none;position:absolute;top:10px;font-size:9.5px;color:#444;line-height:18px}
.foot ul b{font-weight:700;color:#333}
.socials{position:absolute;left:45px;top:14px;display:flex;gap:13px}
.socials i{display:block;width:20px;height:24px;border:2px solid #8a8a8a;border-radius:3px}
.phone{display:flex;align-items:center;gap:6px;font-weight:700;color:#333}
.phone svg{flex:none}
.letter{position:absolute;left:731px;top:10px;width:155px;font-size:9.5px;line-height:18px;color:#444;text-align:justify}
.signup{position:absolute;left:731px;top:76px;display:flex}
.signup input{width:92px;height:27px;border:1px solid #ddd;background:#fff}
.signup button{width:62px;height:27px;border:none;background:var(--red);color:#fff;font:700 10.5px "Open Sans",Arial,sans-serif}
.copy{left:45px;top:1178px;font-size:9.5px;color:#666}
.copy-bg{left:0;top:1168px;width:944px;height:32px;background:var(--foot);border-top:1px solid #ccc}
</style>
</head>
<body>

<header>
  <div class="abs brand"><span class="brand-mark"></span><span class="brand-name">KRVT</span></div>
  <nav class="abs toplinks"><span>Repertoire du personel</span><span>Blogue</span><span>Salle de presse</span><span>Nous joindre</span><span>Francais</span></nav>
  <div class="abs search">Search
    <span class="search-btn"><svg width="29" height="23" viewBox="0 0 29 23"><circle cx="14" cy="10.5" r="4.5" fill="none" stroke="#fff" stroke-width="1.6"/><line x1="17.2" y1="13.7" x2="20" y2="16.5" stroke="#fff" stroke-width="1.8"/></svg></span>
  </div>
  <nav class="abs mainnav"><span>A PROPOS DE L'KRVT</span><span>PROGRAMMES ET FORMAIONS</span><span>ETUDIANTS</span><span>NOUVELLES ET EVENEMENTS</span><span>ENTERPRISES</span></nav>
  <div class="abs header-rule"></div>
</header>

<section class="abs hero">
  <div class="abs hero-scene" role="img" aria-label="Faint grey globe with silhouettes of business people"></div>
  <h1 class="abs">LOREM IPSUM IS SIMPLY DUMMY TEXT</h1>
  <p class="abs">Lorem Ipsum is simply dummy text of the printing and typesetting industry. Lorem Ipsum has been the industry's standard dummy text ever since the 1500s, when an unknown printer took a galley.</p>
</section>

<aside class="abs box who">
  <h2 class="box-title">Vous etes</h2>
  <ul><li>Futur etudiant</li><li>Etudiant actual</li><li>Entreprise</li><li>Employeur</li><li>Postulant</li><li>Medias</li><li>Parenaires</li></ul>
</aside>

<aside class="abs box tv">
  <h2 class="box-title">KRVT.tv</h2>
  <div class="tv-frame" role="img" aria-label="Video still of students in a classroom"></div>
  <div class="tv-bar">
    <svg width="161" height="30" viewBox="0 0 161 30">
      <circle cx="19" cy="15" r="8" fill="none" stroke="#111" stroke-width="1.6"/><path d="M17 11v8l6-4z" fill="#111"/>
      <rect x="32" y="11" width="98" height="8" fill="#111"/><rect x="118" y="12" width="11" height="6" fill="#fff"/>
      <path d="M133 12h3l4-3v12l-4-3h-3z" fill="#111"/><path d="M142 11q3 4 0 8" stroke="#111" fill="none" stroke-width="1.3"/>
      <path d="M147 9h4M147 9v4M155 9h-2M155 9v4M147 21h4M147 21v-4M155 21h-2M155 21v-4" stroke="#111" stroke-width="1.6"/>
    </svg>
  </div>
  <a class="tv-more" href="#">+ de videos</a>
</aside>

<main>
  <h2 class="abs section-title" style="left:257px;top:387px">KRVT &nbsp;devenez les gestionnaires de demain</h2>
  <div class="abs rule" style="left:257px;top:415px;width:412px"></div>
  <p class="abs intro">Lorem Ipsum is simply dummy text of the printing and typesetting industry. Lorem Ipsum has been the industry's standard dummy text ever since the 1500s, when an unknown printer took a galley of type and scrambled .</p>

  <h2 class="abs section-title" style="left:257px;top:482px">Blogue</h2>
  <div class="abs rule" style="left:257px;top:511px;width:412px"></div>
  <article class="abs post" style="left:257px"><div class="thumb" role="img" aria-label="Hands typing on a laptop" style="background:linear-gradient(135deg,#d9d6d8,#8f9097)"></div><div class="date">Lorem 11, <span class="red">2013</span></div><p>Lorem Ipsum is simply dummy text of the print-ing and typesetting .</p><div class="more">Lire la suite</div></article>
  <article class="abs post" style="left:402px"><div class="thumb" role="img" aria-label="Students working together at a table" style="background:linear-gradient(135deg,#c9a48e,#8795a8)"></div><div class="date">Lorem 11, <span class="red">2013</span></div><p>Lorem Ipsum is simply dummy text of the print-ing and typesetting.</p><div class="more">Lire la suite</div></article>
  <article class="abs post" style="left:548px"><div class="thumb" role="img" aria-label="Business meeting around a desk" style="background:linear-gradient(135deg,#e9a866,#e8e0d8 55%,#4c4c52)"></div><div class="date">Lorem 11, <span class="red">2013</span></div><p>Lorem Ipsum is simply dummy text of the print-ing and typesetting .</p><div class="more">Lire la suite</div></article>

  <h2 class="abs section-title" style="left:257px;top:708px">Evenements</h2>
  <div class="abs rule" style="left:257px;top:737px;width:412px"></div>
  <div class="abs event" style="top:749px"><div class="cal"><b>Nov.</b><span>13</span></div><h3>Event A</h3><p>Lorem Ipsum is simply dummy text of the printing and typesetting industry. Lorem Ipsum has been the industry'.</p></div>
  <div class="abs event" style="top:815px"><div class="cal"><b>Nov.</b><span>13</span></div><h3>Event B</h3><p>Lorem Ipsum is simply dummy text of the printing and typesetting industry. Lorem Ipsum has been the industry'.</p></div>
  <a class="abs red" href="#" style="left:257px;top:872px;font-size:10.5px">Tous les evenements</a>
</main>

<aside class="abs box news">
  <h2 class="box-title">Nouvelles</h2>
  <div class="news-item" style="top:36px"><div class="thumb" role="img" aria-label="Black and white office photo" style="background:linear-gradient(135deg,#6d6d6d,#d0d0d0)"></div><p><b>Lorem Ipsum</b> simply dummy text of the printing and typesetting.</p></div>
  <div class="news-item" style="top:112px"><div class="thumb" role="img" aria-label="Students around a table" style="background:linear-gradient(135deg,#b99a7f,#7f93ad)"></div><p><b>Lorem Ipsum</b> simply dummy text of the printing and typesetting.</p></div>
  <div class="news-item" style="top:188px"><div class="thumb" role="img" aria-label="Team meeting" style="background:linear-gradient(135deg,#a29b98,#c88a78)"></div><p><b>Lorem Ipsum</b> simply dummy text of the printing and typesetting.</p></div>
  <div class="news-item" style="top:263px"><div class="thumb" role="img" aria-label="Student with books" style="background:linear-gradient(135deg,#6f8fb0,#d2c3b3)"></div><p><b>Lorem Ipsum</b> simply dummy text of the printing and typesetting.</p></div>
  <div class="news-item" style="top:337px"><div class="thumb" role="img" aria-label="Student studying at a desk" style="background:linear-gradient(135deg,#9a7a6e,#e6e1dc)"></div><p><b>Lorem Ipsum</b> simply dummy text of the printing and typesetting.</p></div>
  <a class="news-more" href="#">de nouvelles</a>
</aside>

<div class="abs rail" aria-label="Partager">
  <div><svg width="16" height="16"><rect x="1" y="1" width="14" height="14" rx="2" fill="none" stroke="#888" stroke-width="1.4"/></svg></div>
  <div><svg width="16" height="16"><rect x="1" y="1" width="14" height="14" rx="2" fill="none" stroke="#888" stroke-width="1.4"/></svg></div>
  <div><svg width="16" height="16"><rect x="1" y="1" width="14" height="14" rx="2" fill="none" stroke="#888" stroke-width="1.4"/></svg></div>
  <div><svg width="18" height="16" viewBox="0 0 18 16"><rect x="4" y="1" width="10" height="4" fill="none" stroke="#888" stroke-width="1.3"/><rect x="1" y="5" width="16" height="7" rx="1.5" fill="none" stroke="#888" stroke-width="1.3"/><rect x="4" y="10" width="10" height="5" fill="#f4f4f4" stroke="#888" stroke-width="1.3"/></svg></div>
  <div><svg width="18" height="16" viewBox="0 0 18 16"><ellipse cx="9" cy="7" rx="7.5" ry="5.5" fill="none" stroke="#888" stroke-width="1.3"/><path d="M4 11l-1 4 4-2.5" fill="none" stroke="#888" stroke-width="1.3"/></svg></div>
</div>

<section class="abs box partners" aria-label="Partenaires">
  <span class="partner" style="width:150px;height:34px"></span>
  <span class="partner" style="width:100px;height:30px"></span>
  <span class="partner" style="width:48px;height:40px"></span>
  <span class="partner" style="width:36px;height:40px"></span>
  <span class="partner" style="width:66px;height:38px;border-radius:50%"></span>
  <span class="partner" style="width:108px;height:30px"></span>
</section>

<footer>
  <div class="abs band">
    <h4 style="left:45px">Suivez-nous</h4>
    <h4 style="left:211px">A propos</h4>
    <h4 style="left:375px">Etudiants</h4>
    <h4 style="left:548px">KRVT</h4>
    <h4 style="left:731px">Infolettre <svg width="17" height="11" viewBox="0 0 17 11" style="vertical-align:-1px;margin-left:4px"><rect x="0.5" y="0.5" width="16" height="10" fill="none" stroke="#fff"/><path d="M0.5 0.5l8 6 8-6" fill="none" stroke="#fff"/></svg></h4>
  </div>
  <div class="abs foot">
    <div class="socials"><i></i><i></i><i></i><i></i></div>
    <ul style="left:211px"><li>A propos de l'KRVT</li><li>Admissions</li><li>Calendrier de L'ecole</li><li>Offres d'emploi</li><li>Offres d'emploi</li><li>Repertoire du personnel</li></ul>
    <ul style="left:375px"><li>Accueil - Etudiants</li><li>Programmes et Formations</li><li>Vie etudiante</li><li style="margin-top:5px"><b>Enterprises</b></li><li><b>Blogue</b></li></ul>
    <ul style="left:548px"><li>12, RUE DES ACACIAS</li><li>Ancienne route, pres du Marche</li><li>des Artisans</li>
      <li class="phone" style="margin-top:6px"><svg width="8" height="16" viewBox="0 0 8 16"><path d="M6 1Q1 3 1 8t5 7" fill="none" stroke="#777" stroke-width="3"/></svg>(221) 30 555 01 23</li>
      <li class="phone" style="margin-top:6px"><svg width="8" height="16" viewBox="0 0 8 16"><path d="M6 1Q1 3 1 8t5 7" fill="none" stroke="#777" stroke-width="3"/></svg>(221) 70 555 04 56</li></ul>
    <p class="letter">Lorem Ipsum is simply dummy text of the printing and typeset-ting industry.</p>
    <form class="signup"><input type="email" aria-label="Courriel"><button type="button">ENVOYER</button></form>
  </div>
  <div class="abs copy-bg"></div>
  <p class="abs copy">© KRVT, 2013 Tous driots reserves</p>
</footer>

</body>
</html>
```